Pharma business needs a catalogue design

Porvel Ltd. is a fast-growing pharma production company, and we need a catalogue design for white label products (as in unbranded ones). We would only want to distribute the catalogue digitally. Attached to this brief is our current product list.

We are also looking to upgrade the look of our product list so this is where you can display your creativity. Feel free to change up the look as much as you like in order to make it look better. You can also make it as long as you wish.

Important: Often times, our customers want to put their logo directly on our product catalogue. You should, therefore, design the catalogue with this in mind and make it simple for us to be able to replace the logo with another one.

The final design should communicate unwavering quality and incredible attention to detail.

Should you have any questions, please do not hesitate to contact us. We understand that any creative process takes joint effort and mutual understanding.

Industry/Entity Type

Pharmaceutical

Font styles to use
Decorative
Script

Colors

Designer to choose colors to be used in the design.

Requirements
Must have
• What is required is to change the photos of each product with tubes/boxes/packaging that just says "your brand here".

```html
<!DOCTYPE html>
<html lang="en">
<head>
<meta charset="utf-8">
<title>Product List 2019 – Vitamins &amp; Minerals</title>
<link href="https://fonts.googleapis.com/css2?family=Lato:wght@300;400;700;900&family=Roboto+Condensed:wght@300;400&family=Oswald:wght@400&display=swap" rel="stylesheet">
<style>
  :root{
    --navy:#2a3f9c;
    --sky:#7fcaf0;
    --sky-line:#86c9ee;
    --stage:#3a3a3a;
    --paper:#ffffff;
    --ink:#1b1b1b;
    --logo-grey:#cfcfcf;
    --field-green:#7d9a5a;
    --field-dark:#4e6a3a;
  }
  *{box-sizing:border-box;margin:0;padding:0}
  html,body{width:1200px;height:728px;overflow:hidden;background:var(--stage)}
  .canvas{position:relative;width:1200px;height:728px}

  .page{position:absolute;top:23px;width:527px;height:682px;background:var(--paper);overflow:hidden}
  .cover{left:83px}
  .catalogue{left:624px}

  /* cover */
  .logo-space{position:absolute;top:66px;left:0;width:100%;text-align:center;
    font-family:'Lato',sans-serif;font-weight:400;font-size:31px;color:var(--logo-grey);letter-spacing:.2px}
  .hero{position:absolute;left:60px;top:150px}
  .cover-title{position:absolute;top:570px;left:0;width:100%;text-align:center;
    font-family:'Lato',sans-serif;font-weight:900;font-size:43px;color:var(--navy);letter-spacing:.5px}
  .year-tab{position:absolute;left:196px;top:624px;width:135px;height:50px;background:var(--navy);
    border-radius:6px 6px 0 0;text-align:center;font-family:'Lato',sans-serif;font-weight:900;
    font-size:40px;line-height:54px;color:#fff}
  .base-band{position:absolute;left:0;bottom:0;width:100%;height:18px;background:var(--navy)}

  /* catalogue page */
  .section-header{position:absolute;top:0;left:0;width:100%;height:33px;background:var(--navy);
    color:#fff;text-align:center;font-family:'Lato',sans-serif;font-weight:700;font-size:17.5px;line-height:33px}
  .product{position:absolute;left:0;width:527px;height:175px}
  .product svg{position:absolute;left:0;top:0}
  .badge-text{position:absolute;left:38px;top:34px;width:26px;text-align:center;color:#fff;
    font-family:'Oswald',sans-serif;font-size:6px;line-height:9.5px}
  .tube-label{position:absolute;left:87px;top:66px;width:43px;text-align:center;
    font-family:'Roboto Condensed',sans-serif;font-size:11.5px;line-height:14.5px;color:var(--ink)}
  .product-name{position:absolute;left:188px;top:29px;font-family:'Lato',sans-serif;font-weight:700;
    font-size:14px;color:var(--navy)}
  .spec{position:absolute;top:60px;display:grid;grid-template-columns:62px auto;
    font-family:'Roboto Condensed',sans-serif;font-weight:400;font-size:7px;line-height:9.5px;color:var(--ink)}
  .spec.divided{border-left:.8px solid var(--ink);padding-left:9px}
  .dose-pill{position:absolute;left:182px;top:148px;width:150px;height:21px;background:var(--navy);
    border-radius:8px;color:#fff;text-align:center;font-family:'Oswald',sans-serif;font-size:10px;line-height:21px}
  .footer-tab{position:absolute;left:216px;bottom:17px;width:95px;height:13px;background:var(--navy);border-radius:5px 5px 0 0}
  .footer-band{position:absolute;left:0;bottom:0;width:100%;height:14px;background:var(--navy)}
</style>
</head>
<body>
<div class="canvas">

  <section class="page cover">
    <div class="logo-space">SPACE FOR BRAND LOGO</div>
    <svg class="hero" width="410" height="410" viewBox="0 0 410 410">
      <defs>
        <linearGradient id="meadow" x1="0" y1="0" x2="0" y2="1">
          <stop offset="0" stop-color="#c9d3c4"/>
          <stop offset=".35" stop-color="var(--field-green)"/>
          <stop offset=".8" stop-color="var(--field-dark)"/>
          <stop offset="1" stop-color="#8a8a4a"/>
        </linearGradient>
      </defs>
      <circle cx="206" cy="209" r="195" fill="url(#meadow)" role="img" aria-label="Photo: woman leaping from a log into a green hillside meadow"/>
      <circle cx="195" cy="205" r="194" fill="none" stroke="var(--navy)" stroke-width="2.5"/>
    </svg>
    <div class="cover-title">PRODUCT LIST</div>
    <div class="base-band"></div>
    <div class="year-tab">2019</div>
  </section>

  <section class="page catalogue">
    <header class="section-header">VITAMINS &amp; MINERALS - EFFERVESCENT PRODUCTS</header>

    <!-- product 1 -->
    <article class="product" style="top:60px">
      <svg width="527" height="175" viewBox="0 0 527 175">
        <defs>
          <linearGradient id="tubeShade" x1="0" x2="1">
            <stop offset="0" stop-color="#dcdcdc"/><stop offset=".35" stop-color="#ffffff"/><stop offset="1" stop-color="#cfcfcf"/>
          </linearGradient>
        </defs>
        <path d="M107 22 H480 Q486 22 486 28 V153 Q486 159 480 159 H107" fill="none" stroke="var(--sky-line)" stroke-width="1.6"/>
        <circle cx="104" cy="90" r="71" fill="none" stroke="var(--navy)" stroke-width="1.6"/>
        <circle cx="107" cy="91" r="69" fill="var(--sky)"/>
        <circle cx="51" cy="46" r="18.5" fill="var(--navy)"/>
        <rect x="89" y="12" width="39" height="150" rx="6" fill="url(#tubeShade)"/>
        <rect x="87" y="2" width="43" height="18" rx="3" fill="url(#tubeShade)"/>
      </svg>
      <div class="badge-text">20<br>TABLETS<br>IN TUBE</div>
      <div class="tube-label">Your<br>Brand<br>Here</div>
      <h2 class="product-name">A-Z &nbsp;+Lutein and Selenium</h2>
      <div class="spec" style="left:188px">
        <span>Calcium</span><span>160 mg</span><span>Magnesium</span><span>60 mg</span><span>Vitamin C</span><span>60 mg</span><span>Vitamin B3</span><span>18 mg</span><span>Ferrum</span><span>10 mg</span><span>Vitamin E</span><span>10 mg</span><span>Pantothenic acid</span><span>6 mg</span><span>Zinc</span><span>5 mg</span>
      </div>
      <div class="spec divided" style="left:281px">
        <span>Vitamin B2</span><span>2,97 mg</span><span>Vitamin B6</span><span>2 mg</span><span>Vitamin B1</span><span>1,4 mg</span><span>Vitamin A</span><span>800 µg</span><span>Copper</span><span>0,5 mg</span><span>Manganese</span><span>0,4 mg</span><span>Folat</span><span>200 µg</span><span>Vitamin H</span><span>150 µg</span>
      </div>
      <div class="spec divided" style="left:385px">
        <span>Iodine</span><span>100 µg</span><span>Lutein</span><span>50 µg</span><span>Vitamin K</span><span>130 µg</span><span>Selenium</span><span>30 µg</span><span>Cromium</span><span>25 µg</span><span>Molybdenum</span><span>25 µg</span><span>Vitamin D3</span><span>5 µg</span><span>Vitamin B12</span><span>1 µg</span>
      </div>
      <div class="dose-pill">4000 MG/TABLET (CITRUS FLAVOR)</div>
    </article>

    <!-- product 2 -->
    <article class="product" style="top:264px">
      <svg width="527" height="175" viewBox="0 0 527 175">
        <path d="M107 22 H480 Q486 22 486 28 V153 Q486 159 480 159 H107" fill="none" stroke="var(--sky-line)" stroke-width="1.6"/>
        <circle cx="104" cy="90" r="71" fill="none" stroke="var(--navy)" stroke-width="1.6"/>
        <circle cx="107" cy="91" r="69" fill="var(--sky)"/>
        <circle cx="51" cy="46" r="18.5" fill="var(--navy)"/>
        <rect x="89" y="12" width="39" height="150" rx="6" fill="url(#tubeShade)"/>
        <rect x="87" y="2" width="43" height="18" rx="3" fill="url(#tubeShade)"/>
      </svg>
      <div class="badge-text">20<br>TABLETS<br>IN TUBE</div>
      <div class="tube-label">Your<br>Brand<br>Here</div>
      <h2 class="product-name">MULTIVITAMINS +Biotin</h2>
      <div class="spec" style="left:191px;top:62px">
        <span>Vitamin A</span><span>900 µg</span><span>Vitamin E</span><span>6,90 mg</span><span>Vitamin B1</span><span>1,80 mg</span><span>Vitamin B2</span><span>1,45 mg</span><span>Vitamin B6</span><span>1,70 mg</span><span>Vitamin B12</span><span>5 µg</span><span>Vitamin C</span><span>75 mg</span>
      </div>
      <div class="spec divided" style="left:290px;top:62px;padding-left:13px;height:76px">
        <span>Folic acid</span><span>200 µg</span><span>Nicotinamide</span><span>20 mg</span><span>Vitamin D3</span><span>5 µg</span><span>Vitamin B5</span><span>10 mg</span><span>Beta Carotene</span><span>0,50 mg</span><span>Biotin</span><span>50 µg</span>
      </div>
      <div class="dose-pill">4000 MG/TABLET (ORANGE FLAVOR)</div>
    </article>

    <!-- product 3 -->
    <article class="product" style="top:468px">
      <svg width="527" height="175" viewBox="0 0 527 175">
        <path d="M107 22 H480 Q486 22 486 28 V153 Q486 159 480 159 H107" fill="none" stroke="var(--sky-line)" stroke-width="1.6"/>
        <circle cx="104" cy="90" r="71" fill="none" stroke="var(--navy)" stroke-width="1.6"/>
        <circle cx="107" cy="91" r="69" fill="var(--sky)"/>
        <circle cx="51" cy="46" r="18.5" fill="var(--navy)"/>
        <rect x="89" y="12" width="39" height="150" rx="6" fill="url(#tubeShade)"/>
        <rect x="87" y="2" width="43" height="18" rx="3" fill="url(#tubeShade)"/>
      </svg>
      <div class="badge-text">20<br>TABLETS<br>IN TUBE</div>
      <div class="tube-label">Your<br>Brand<br>Here</div>
      <h2 class="product-name">ACTIVE + Q10</h2>
      <div class="spec" style="left:189px;top:62px">
        <span>Vitamin E</span><span>16,50 mg</span><span>Vitamin B1</span><span>2,60 mg</span><span>Vitamin B2</span><span>1,90 mg</span><span>Vitamin B6</span><span>4,00 mg</span><span>Vitamin B12</span><span>4,95 µg</span><span>Vitamin C</span><span>160 mg</span><span>Folic acid</span><span>200 µg</span>
      </div>
      <div class="spec divided" style="left:283px;top:62px;padding-left:5px;height:76px">
        <span>Nicotinamide</span><span>19,80 mg</span><span>Vitamin D3</span><span>5 µg</span><span>Copper</span><span>0,45 mg</span><span>Iron</span><span>2,70 mg</span><span>Magnesium</span><span>60 mg</span><span>Zinc</span><span>2,70 mg</span>
      </div>
      <div class="spec divided" style="left:382px;top:62px;padding-left:5px;height:76px">
        <span>Manganese</span><span>0,90 mg</span><span>Beta Carotene</span><span>0,5 mg</span><span>Coenzyme Q10.</span><span>2,00 mg</span>
      </div>
      <div class="dose-pill">4000 MG/TABLET (ORANGE FLAVOR)</div>
    </article>

    <div class="footer-tab"></div>
    <div class="footer-band"></div>
  </section>

</div>
</body>
</html>
```